Female Pest Controller needs awesome business cards

I need a logo design for a Pest Control service - something that appeals to 'nature' & safe, with the use of the colour green. I am also female
New Business Name is 'Bug Bolted'
appeals to women

Target Market(s)

Domestic Households & Local Businesses

Industry/Entity Type

Pest Control

Contact Information for Business Card

Rowena Calderitt
0438526190
ABN 61 847 530 218
PMT7309145538
Spiders Cockroaches, Ants, Silverfish, Fleas, Rodents

Font styles to use
Decorative

Colors
abd036
aaaaaa
5c5c5c

Requirements
Should not have
• Pics of dead insects, prefer nature inspired designs, frogs, trees etc
• Have attached old log & business name ( now my ex's business) Brookhaven Pest Solutions -

```html
<!DOCTYPE html>
<html lang="en">
<head>
<meta charset="utf-8">
<title>Bug Bolted – Business Card</title>
<link href="https://fonts.googleapis.com/css2?family=Cinzel:wght@600&family=Montserrat:wght@400;600&display=swap" rel="stylesheet">
<style>
  :root{
    --green:#abd036;
    --green-light:#bcdf52;
    --grey-light:#aaaaaa;
    --grey-dark:#5c5c5c;
    --grey-mid:#6e6e6e;
    --white:#ffffff;
    --paper:#f4f4f4;
    --backdrop:#e6e6e6;
  }
  *{margin:0;padding:0;box-sizing:border-box}
  html,body{width:1200px;height:914px;overflow:hidden;background:var(--backdrop)}
  .stage{position:relative;width:1200px;height:914px;display:flex;justify-content:center;align-items:center;gap:80px}
  .card{position:relative;width:360px;height:630px;overflow:hidden;box-shadow:0 10px 30px rgba(0,0,0,.18)}

  /* front */
  .card-front{background:linear-gradient(180deg,var(--white),var(--paper))}
  .front-wave{position:absolute;left:0;bottom:0;width:360px;height:330px}
  .brand-lockup{position:absolute;top:160px;left:0;width:100%;display:flex;align-items:center;justify-content:center;gap:12px}
  .brand-dot{width:26px;height:26px;border-radius:50%;background:var(--green)}
  .brand-name{font-family:"Montserrat",sans-serif;font-weight:600;font-size:34px;color:var(--grey-dark);letter-spacing:.5px}
  .person{position:absolute;top:400px;width:100%;text-align:center;font-family:"Montserrat",sans-serif}
  .person-name{font-weight:600;font-size:22px;color:var(--grey-mid);letter-spacing:1px;text-transform:uppercase}
  .person-role{font-weight:400;font-size:15px;color:var(--white);margin-top:2px}
  .contact-icons{position:absolute;top:480px;width:100%;display:flex;justify-content:center;gap:16px}
  .contact-icons svg{width:18px;height:18px}
  .contact-list{position:absolute;top:512px;width:100%;text-align:center;font-family:"Montserrat",sans-serif;font-size:15px;line-height:23px;color:var(--white);list-style:none}

  /* back */
  .card-back{background:linear-gradient(160deg,var(--grey-mid),var(--grey-dark))}
  .back-title{position:absolute;left:50%;top:50%;transform:translate(-70%,-50%) rotate(90deg);font-family:"Cinzel",serif;font-weight:600;font-size:40px;color:var(--white);letter-spacing:3px;white-space:nowrap}
  .back-mark{position:absolute;left:220px;top:120px;width:56px;height:56px;border-radius:50%;background:var(--green)}
</style>
</head>
<body>
<main class="stage">
  <section class="card card-front">
    <svg class="front-wave" viewBox="0 0 360 330" aria-hidden="true">
      <path d="M0 110 Q170 40 360 0 L360 330 L0 330 Z" fill="var(--green)"/>
    </svg>
    <div class="brand-lockup">
      <span class="brand-dot"></span>
      <span class="brand-name">Bug Bolted</span>
    </div>
    <div class="person">
      <p class="person-name">Rowena Calderitt</p>
      <p class="person-role">Director</p>
    </div>
    <div class="contact-icons">
      <svg viewBox="0 0 24 24" aria-label="phone"><path d="M7 3 L10 3 L11 8 L9 9.5 Q10.5 13.5 14.5 15 L16 13 L21 14 L21 17 Q21 20 18 20 Q5 19 4 6 Q4 3 7 3Z" fill="var(--white)"/></svg>
      <svg viewBox="0 0 24 24" aria-label="email"><rect x="2" y="5" width="20" height="14" fill="var(--white)"/><path d="M2 5 L12 13 L22 5" fill="none" stroke="var(--green)" stroke-width="1.5"/></svg>
      <svg viewBox="0 0 24 24" aria-label="website"><g fill="none" stroke="var(--white)" stroke-width="1.6"><circle cx="12" cy="12" r="9"/><ellipse cx="12" cy="12" rx="4" ry="9"/><path d="M3 12 H21 M5 7 H19 M5 17 H19"/></g></svg>
    </div>
    <ul class="contact-list">
      <li>0438526190</li>
      <li>rowena@bugbolted.com</li>
      <li>www.bugbolted.com</li>
    </ul>
  </section>

  <section class="card card-back">
    <span class="back-mark"></span>
    <h1 class="back-title">BUG BOLTED</h1>
  </section>
</main>
</body>
</html>
```